Cobra Vane Systems Website Revamp

We need a full website for the oil and gas sector to showcase our company and our technology/services we provide to larger corporations. We want our website represent innovation and identity.

Background:

We are a service based company that specializes in:

- well services, and
-permanent applications
**(Please be aware that these are two different aspects to the oil and gas sector, both of which we supply to our customers)

We provide a wide range of jet pump technologies to address under performing reservoirs or problematic well producing conditions. We have field operations currently in: Canada, Oman, and Australia with efforts currently underway to expand in other markets. Therefore are needing a website to help promote a better comprehension of what we do and how we can solve their well issues. We are looking for

1.) Identity;
2.) Emphasis on better comprehension of our services for our clients to relate to us as a solution to their needs;
3.) User friendly interface - but new and exciting in this digital age .

Some examples of websites we like:

http://brindlowinc.com/how-we-work/
http://www.qorvantix.com/qorvan-system/
https://velmorafield.com/

Videos of our technologies:

https://www.clipvarro.com/watch?v=519KdpQWzRe
https://www.clipvarro.com/watch?v=t7NBwuhsp43

Target Market(s)

Petroleum Industry Clients

Coding

Coded - Design and coding required

Number of Pages Required

5+ page

Colors

Designer to choose colors to be used in the design.

Requirements
Must have
• See Project Description, and feel free to contact us with any questions/inquiries!
Nice to have
• Our color scheme is generally 'blue', to depict jet pumps (our service). However, we are open to ideas and artistic interpretation. Grayscale/offset colors/highlight colors etc.

```html
<!DOCTYPE html>
<html lang="en">
<head>
<meta charset="utf-8">
<title>Bedrock Flow Partners</title>
<link href="https://fonts.googleapis.com/css2?family=Poppins:wght@400;500;600&family=Roboto:wght@400;700&family=Open+Sans:wght@300;400&display=swap" rel="stylesheet">
<style>
:root{
  --white:#ffffff;
  --ink:#111111;
  --heading:#2b2b2b;
  --body:#333333;
  --muted:#666666;
  --section-grey:#f1f1f6;
  --quote-mark:#eeeef3;
  --footer-blue:#1a4de8;
  --arrow-a:#3d3f8f;
  --arrow-b:#5a5fae;
  --btn-a:#6a96c6;
  --btn-b:#0b2e5e;
  --pad-green:#3aa83a;
  --pad-grey:#d9dde2;
}
*{margin:0;padding:0;box-sizing:border-box}
html,body{width:1200px;height:1200px;overflow:hidden;background:var(--white)}
.page{position:relative;width:1200px;height:1200px}

/* feature band */
.feature{position:absolute;left:0;top:0;width:1200px;height:414px;background:var(--white)}
.pad-illustration{position:absolute;left:152px;top:0;width:536px;height:156px;
  background:linear-gradient(160deg,var(--pad-green) 0%,var(--pad-green) 35%,var(--pad-grey) 36%,#f4f5f6 100%)}
.feature-title{position:absolute;left:104px;top:193px;width:220px;text-align:center;
  font-family:"Roboto",Arial,sans-serif;font-weight:700;font-size:16.5px;line-height:24px;color:var(--ink)}
.btn-learn{position:absolute;left:123px;top:285px;width:171px;height:38px;border-radius:19px;
  background:linear-gradient(90deg,var(--btn-a),var(--btn-b));color:var(--white);
  font-family:"Open Sans",Arial,sans-serif;font-weight:400;font-size:13px;
  display:flex;align-items:center;justify-content:center;text-decoration:none}
.pad-illustration-right{position:absolute;left:776px;top:0;width:286px;height:298px;
  background:linear-gradient(170deg,#f7f7f8 0%,var(--pad-green) 20%,var(--pad-green) 42%,#eef0f2 45%,#f7f7f8 100%)}

/* testimonials */
.testimonials{position:absolute;left:0;top:414px;width:1200px;height:633px;background:var(--section-grey)}
.eyebrow{position:absolute;left:0;top:74px;width:1200px;text-align:center;
  font-family:"Poppins",sans-serif;font-weight:500;font-size:13.5px;letter-spacing:1.6px;color:#555}
.section-title{position:absolute;left:0;top:96px;width:1200px;text-align:center;
  font-family:"Poppins",sans-serif;font-weight:600;font-size:29px;color:var(--heading)}
.quote-card{position:absolute;left:368px;top:172px;width:480px;height:254px;background:var(--white);
  box-shadow:0 6px 30px rgba(40,40,80,.06)}
.quote-mark{position:absolute;font-family:"Poppins",sans-serif;font-weight:600;font-size:90px;line-height:1;color:var(--quote-mark)}
.quote-open{left:8px;top:4px}
.quote-close{right:10px;top:186px}
.quote-text{position:absolute;left:40px;top:53px;width:400px;text-align:center;
  font-family:"Poppins",sans-serif;font-size:13px;line-height:22.4px;color:var(--body)}
.author-name{position:absolute;left:0;top:141px;width:480px;text-align:center;
  font-family:"Poppins",sans-serif;font-weight:600;font-size:10.5px;letter-spacing:.8px;color:#222}
.author-role{position:absolute;left:0;top:161px;width:480px;text-align:center;
  font-family:"Poppins",sans-serif;font-size:11.5px;letter-spacing:.5px;color:var(--muted)}
.author-photo{position:absolute;left:568px;top:387px;width:80px;height:80px;
  background:linear-gradient(135deg,#9a6a42,#c9c2b6 60%,#e8e6e2);box-shadow:0 10px 30px rgba(0,0,0,.12)}
.slider-arrow{position:absolute;top:280px;width:40px;height:40px;
  background:linear-gradient(135deg,var(--arrow-a),var(--arrow-b));display:flex;align-items:center;justify-content:center}
.slider-prev{left:346px}
.slider-next{left:827px}

/* footer */
.site-footer{position:absolute;left:0;top:1047px;width:1200px;height:153px;background:var(--footer-blue)}
.social{position:absolute;top:17px;width:30px;height:30px;border:2px solid var(--white);border-radius:50%}
.social-a{left:567px}
.social-b{left:603px}
.footer-nav a{position:absolute;top:68px;transform:translateX(-50%);white-space:nowrap;
  font-family:"Roboto",Arial,sans-serif;font-size:13px;color:var(--white);text-decoration:none}
.copyright{position:absolute;left:0;top:107px;width:1200px;text-align:center;
  font-family:"Open Sans",Arial,sans-serif;font-size:11px;color:var(--white)}
</style>
</head>
<body>
<div class="page">

  <section class="feature">
    <div class="pad-illustration" role="img" aria-label="Illustration of a green well pad with pump jacks and curved horizontal wellbores below"></div>
    <h3 class="feature-title">BFP Jet Pump Well Pad Development</h3>
    <a class="btn-learn" href="#">LEARN MORE</a>
    <div class="pad-illustration-right" role="img" aria-label="Illustration of a green well pad with jet pump units, a pressure vessel and horizontal wellbores"></div>
  </section>

  <section class="testimonials">
    <p class="eyebrow">TESTIMONIAL</p>
    <h2 class="section-title">Our Success Stories</h2>

    <div class="quote-card">
      <span class="quote-mark quote-open">“</span>
      <span class="quote-mark quote-close">”</span>
      <p class="quote-text">Lorem Ipsum is simply dummy text of the printing and typesetting industry. Lorem Ipsum has been the industry's standard dummy text ever since the 1500s.</p>
      <p class="author-name">ALAN REYES</p>
      <p class="author-role">UI/UX Designer</p>
    </div>
    <div class="author-photo" role="img" aria-label="Portrait photo of the client at a desk with a computer"></div>

    <a class="slider-arrow slider-prev" href="#" aria-label="Previous">
      <svg width="10" height="12" viewBox="0 0 10 12"><path d="M8 0 L2 6 L8 12 Z" fill="#fff"/></svg>
    </a>
    <a class="slider-arrow slider-next" href="#" aria-label="Next">
      <svg width="10" height="12" viewBox="0 0 10 12"><path d="M2 0 L8 6 L2 12 Z" fill="#fff"/></svg>
    </a>
  </section>

  <footer class="site-footer">
    <span class="social social-a" aria-label="Social profile"></span>
    <span class="social social-b" aria-label="Social profile"></span>
    <nav class="footer-nav">
      <a href="#" style="left:422px">What we do</a>
      <a href="#" style="left:524px">Who we are</a>
      <a href="#" style="left:653px">Product &amp; service</a>
      <a href="#" style="left:779px">Contact Us</a>
    </nav>
    <p class="copyright">© Copyright 2015 - Bedrock Flow Partners</p>
  </footer>

</div>
</body>
</html>
```